Business card

We are looking for a creative person to deigns our company business card.

Target Market(s)

College age student

Industry/Entity Type

Accommodation

Contact Information for Business Card

We want a fun, clean and sophisticated design. It should look good, but more importantly the information should be legible.

Font styles to use
Serif
Sans Serif
Other font styles liked:
• Open Sans ,

Colors
33a6d7

Requirements
Must have
• Must have a young and memorable message. Be legible.
• Our logo on the back on a solid blue , please find color and logo attached
• LodgeBridgely.net on the back.
Nice to have
• I would like to have couple of different fonts on the LodgeBridgely.net on the back of the cards with a solid blue.

```html
<!DOCTYPE html>
<html lang="en">
<head>
<meta charset="utf-8">
<title>LodgeBridgely – Business Card</title>
<link href="https://fonts.googleapis.com/css2?family=Arimo:wght@400;700&family=EB+Garamond:wght@400&display=swap" rel="stylesheet">
<style>
  :root {
    --backdrop: #e6e7e8;
    --card-dark: #1c1c1c;
    --card-blue: #33a6d7;
    --ink: #ffffff;
    --rule: #bdbdbd;
  }
  * { margin: 0; padding: 0; box-sizing: border-box; }
  html, body { width: 1200px; height: 800px; overflow: hidden; background: var(--backdrop); }
  .canvas { position: relative; width: 1200px; height: 800px; }
  .card {
    position: absolute; left: 327px; width: 535px; height: 305px;
    color: var(--ink); overflow: hidden;
  }
  .card--back { top: 34px; background: var(--card-blue); }
  .card--front { top: 434px; height: 304px; background: var(--card-dark); }

  .back-frame {
    position: absolute; left: 44px; top: 26px; right: 29px; bottom: 32px;
    border: 2.5px solid var(--ink);
  }
  .brand {
    position: absolute; display: flex; align-items: center;
    transform: translate(-50%, -50%); white-space: nowrap;
    font-family: "Arimo", Arial, sans-serif; font-weight: 700; line-height: 1;
  }
  .brand-square { background: var(--ink); flex: none; }
  .card--back .brand { left: 270px; top: 152px; font-size: 30px; gap: 14px; }
  .card--back .brand-square { width: 26px; height: 26px; }
  .card--front .brand { left: 426px; top: 158px; font-size: 20px; gap: 9px; }
  .card--front .brand-square { width: 17px; height: 17px; }

  .person-name {
    position: absolute; left: 39px; top: 132px;
    font-family: "EB Garamond", Georgia, serif; font-weight: 400; font-size: 39px; line-height: 1;
  }
  .person-role {
    position: absolute; left: 81px; top: 167px;
    font-family: "EB Garamond", Georgia, serif; font-weight: 400; font-size: 19px; line-height: 1;
  }
  .divider { position: absolute; left: 25px; top: 194px; width: 490px; height: 1px; background: var(--rule); }

  .contact {
    position: absolute; font-family: "EB Garamond", Georgia, serif;
    font-size: 15px; line-height: 1;
  }
  .contact--phone { left: 73px; top: 217px; }
  .contact--email { left: 73px; top: 245px; }
  .icon { position: absolute; fill: var(--ink); }
  .icon--phone { left: 38px; top: 213px; }
  .icon--mail { left: 37px; top: 247px; }
  .icon--pin { left: 311px; top: 205px; }
  .addresses {
    position: absolute; left: 346px; top: 204px;
    font-family: "EB Garamond", Georgia, serif; font-size: 14.5px; line-height: 19px;
  }
  .addresses p + p { margin-top: 4px; }

  .foot-bar { position: absolute; top: 293px; height: 9px; background: var(--ink); }
  .foot-bar--left { left: 0; width: 158px; }
  .foot-bar--right { left: 377px; width: 158px; }
  .site-address {
    position: absolute; left: 267px; top: 290px; transform: translateX(-50%);
    font-family: "Arimo", Arial, sans-serif; font-weight: 400; font-size: 13px; line-height: 1;
  }
</style>
</head>
<body>
<main class="canvas">
  <section class="card card--back" aria-label="Card back">
    <div class="back-frame"></div>
    <div class="brand"><span class="brand-square"></span>LodgeBridgely.net</div>
  </section>

  <section class="card card--front" aria-label="Card front">
    <div class="brand"><span class="brand-square"></span>LodgeBridgely</div>

    <h1 class="person-name">Name here</h1>
    <p class="person-role">Founder</p>
    <div class="divider"></div>

    <svg class="icon icon--phone" width="18" height="18" viewBox="0 0 24 24" aria-hidden="true">
      <path d="M6.6 10.8a15.1 15.1 0 0 0 6.6 6.6l2.2-2.2c.3-.3.7-.4 1-.2 1.1.4 2.3.6 3.6.6.6 0 1 .4 1 1V20c0 .6-.4 1-1 1A17 17 0 0 1 3 4c0-.6.4-1 1-1h3.5c.6 0 1 .4 1 1 0 1.3.2 2.5.6 3.6.1.3 0 .7-.2 1z"/>
    </svg>
    <span class="contact contact--phone">555-014-2286</span>

    <svg class="icon icon--mail" width="22" height="14" viewBox="0 0 22 14" aria-hidden="true">
      <rect x="0.75" y="0.75" width="20.5" height="12.5" fill="none" stroke="#fff" stroke-width="1.5"/>
      <path d="M1 1l10 7 10-7" fill="none" stroke="#fff" stroke-width="1.5"/>
    </svg>
    <span class="contact contact--email">mara@harborlanegoods.com</span>

    <svg class="icon icon--pin" width="16" height="24" viewBox="0 0 16 24" aria-hidden="true">
      <path d="M8 0a8 8 0 0 0-8 8c0 6 8 16 8 16s8-10 8-16a8 8 0 0 0-8-8zm0 11a3 3 0 1 1 0-6 3 3 0 0 1 0 6z"/>
    </svg>
    <div class="addresses">
      <p>Harbor Lane North 20417<br>cedar ave n.lakeview</p>
      <p>Harbor Lane central 3310<br>9th ave s, lakeview</p>
    </div>

    <div class="foot-bar foot-bar--left"></div>
    <span class="site-address">LodgeBridgely.net</span>
    <div class="foot-bar foot-bar--right"></div>
  </section>
</main>
</body>
</html>
```